Heron Payments Business card refresh

Need a new design of our business card The info is not what is on these cards i sent this for a reference. I can email all the info over
Info would be Dale Merton Chief HERON is the title. our new address is 47615 Birch Hollow Ln. Westlake Village Ca 93027 Cell number is 805-555-0147 Work number is 855-555-0182 ext 212 Dale@heronpaylane.example is my email address
Target Market(s)
Merchant Services all businesses that take credit cards
Industry/Entity Type
Merchant Services / Credit Card processing
Contact Information for Business Card
Need a new design of our business card The info is not what is on these cards i sent this for a reference. I can email all the info over Info would be Dale Merton Chief HERON is the title. our new address is 47615 Birch Hollow Ln. Westlake Village Ca 93027 Cell number is 805-555-0147 Work number is 855-555-0182 ext 212 Dale@heronpaylane.example is my email address
Requirements
Must have
- My logo and colors from my brand guidelines
Nice to have
- i sent some designs just need a new refresh
Should not have
- nothing specific

```html
<!DOCTYPE html>
<html lang="en">
<head>
<meta charset="utf-8">
<title>Heron Payments – Business Card</title>
<link rel="stylesheet" href="https://fonts.googleapis.com/css2?family=Montserrat:wght@400;500;700;800&display=swap">
<style>
  :root {
    --charcoal: #2b2f33;
    --charcoal-deep: #23272a;
    --lime: #8dc21f;
    --white: #ffffff;
    --ink: #2a2e31;
    --backdrop: #3a3a3a;
  }
  * { box-sizing: border-box; margin: 0; padding: 0; }
  html, body { width: 1200px; height: 1186px; overflow: hidden; }
  body {
    background: var(--backdrop);
    font-family: "Montserrat", sans-serif;
    position: relative;
  }
  .card {
    position: absolute;
    left: 150px;
    width: 900px;
    height: 514px;
    border-radius: 24px;
    overflow: hidden;
  }
  .card-back { top: 52px; background: var(--charcoal); color: var(--white); }
  .card-front { top: 620px; background: var(--white); color: var(--ink); }
  .card svg.shapes { position: absolute; inset: 0; width: 900px; height: 514px; }

  .brand-name {
    position: absolute; left: 70px;
    display: flex; align-items: center; gap: 16px;
    font-weight: 700; font-size: 56px; line-height: 1;
  }
  .brand-dot { width: 22px; height: 22px; border-radius: 50%; background: var(--lime); flex: none; }
  .card-back .brand-name { top: 120px; color: var(--white); }
  .card-front .brand-name { top: 190px; color: var(--ink); }

  .services {
    position: absolute; left: 70px; top: 250px;
    display: grid; grid-template-columns: auto auto; column-gap: 40px; row-gap: 10px;
    font-size: 21px; font-weight: 400; list-style: none;
  }
  .services li::before {
    content: ""; display: inline-block; width: 8px; height: 8px; border-radius: 50%;
    background: var(--lime); margin-right: 12px; vertical-align: middle;
  }
  .slogan {
    position: absolute; left: 0; right: 0; top: 448px; text-align: center;
    font-weight: 800; font-size: 30px; letter-spacing: 1px; color: var(--white);
  }

  .referral {
    position: absolute; left: 640px; top: 32px; color: var(--white);
    font-size: 21px; line-height: 1.25;
  }
  .referral strong { font-weight: 700; }
  .rule { position: absolute; left: 70px; top: 292px; width: 760px; height: 2px; background: var(--lime); }
  .person { position: absolute; left: 70px; top: 306px; }
  .person-name { font-weight: 800; font-size: 34px; color: var(--lime); line-height: 1.1; }
  .person-title { font-size: 21px; font-weight: 500; margin-bottom: 8px; }
  .contacts { list-style: none; font-size: 18px; line-height: 25px; }
  .contacts li { display: flex; align-items: center; gap: 12px; }
  .contacts svg { width: 15px; height: 15px; flex: none; }
  .address {
    position: absolute; right: 70px; top: 320px; text-align: right;
    font-size: 20px; line-height: 1.3;
  }
</style>
</head>
<body>

<section class="card card-back" aria-label="Business card back">
  <svg class="shapes" viewBox="0 0 900 514" aria-hidden="true">
    <polygon points="0,425 900,395 900,514 0,514" fill="var(--lime)"/>
  </svg>
  <p class="brand-name"><span class="brand-dot"></span>Heron Payments</p>
  <ul class="services">
    <li>Credit Card Processing</li>
    <li>White-glove Support</li>
    <li>Same Day Approval</li>
    <li>Merchant Funding</li>
    <li>Check Guarantee</li>
    <li>ACH Deposits</li>
    <li>Loyalty Cards</li>
    <li>ATM Sales</li>
  </ul>
  <p class="slogan">BEST RATES, BEST SERVICES - GUARANTEED</p>
</section>

<section class="card card-front" aria-label="Business card front">
  <svg class="shapes" viewBox="0 0 900 514" aria-hidden="true">
    <path d="M470,0 H900 V150 H650 C600,150 585,110 560,70 C535,30 510,0 470,0 Z" fill="var(--lime)"/>
    <polygon points="595,470 900,440 900,514 595,514" fill="var(--charcoal-deep)"/>
    <polygon points="625,467 900,440 900,514 625,514" fill="var(--lime)"/>
  </svg>
  <p class="referral">Ask About Our<br><strong>Merchant Referral</strong><br>Program</p>
  <p class="brand-name"><span class="brand-dot"></span>Heron Payments</p>
  <div class="rule"></div>
  <div class="person">
    <p class="person-name">Dale Merton</p>
    <p class="person-title">Chief HERON</p>
    <ul class="contacts">
      <li><svg viewBox="0 0 16 16"><rect x="4" y="1" width="8" height="14" rx="1.5" fill="none" stroke="var(--lime)" stroke-width="1.6"/></svg>805-555-0147</li>
      <li><svg viewBox="0 0 16 16"><path d="M1,6 C1,2 15,2 15,6 L12,7 L11,5 H5 L4,7 Z M3,9 H13 V14 H3 Z" fill="var(--lime)"/></svg>855-555-0182 ext 212</li>
      <li><svg viewBox="0 0 16 16"><rect x="1" y="3" width="14" height="10" fill="var(--lime)"/><path d="M1,3 L8,9 L15,3" fill="none" stroke="var(--white)" stroke-width="1.3"/></svg>Dale@heronpaylane.example</li>
      <li><svg viewBox="0 0 16 16"><circle cx="8" cy="8" r="7" fill="var(--lime)"/><path d="M1,8 H15 M8,1 C4,5 4,11 8,15 M8,1 C12,5 12,11 8,15" fill="none" stroke="var(--white)" stroke-width="1"/></svg>www.heronpaylane.example</li>
    </ul>
  </div>
  <p class="address">47615 Birch Hollow Ln. Westlake<br>Village Ca 93027</p>
</section>

</body>
</html>
```